Webdesign für Rheinau Vita Forschungsbund e.V.
Zielgruppe
Vereinsmitglieder aus der Bio-Tech-Branche, Öffentlichkeit
Aufgabenstellung
Wir benötigen ein Webdesign für die Website des Rheinau Vita Forschungsbund e.V., zu liefern als PSD-Datei.

```html
<!DOCTYPE html>
<html lang="de">
<head>
<meta charset="utf-8">
<title>Rheinau Vita Forschungsbund e.V.</title>
<link href="https://fonts.googleapis.com/css2?family=Arimo:wght@400;700&display=swap" rel="stylesheet">
<style>
:root{
  --teal:#3a9fb3;
  --teal-dark:#2f8ea3;
  --teal-light:#5cb8c9;
  --text:#333;
  --muted:#555;
  --rule:#3a9fb3;
  --bg-top:#ffffff;
  --bg-bottom:#e7eff4;
  --footer:#8a8f94;
}
*{margin:0;padding:0;box-sizing:border-box}
html,body{width:1200px;height:881px;overflow:hidden}
body{
  font-family:"Arimo",Arial,sans-serif;
  color:var(--text);
  background:linear-gradient(180deg,var(--bg-top) 0%,#f4f8fa 60%,var(--bg-bottom) 100%);
  position:relative;
}
.page{
  position:absolute;left:44px;top:0;width:1109px;height:811px;
  background:#fff;border:1px solid #dde6ea;border-top:none;
}
.header{position:absolute;left:0;top:0;width:100%;height:200px;background:#fff}
.header-photo{
  position:absolute;right:0;top:0;width:665px;height:200px;
  background:linear-gradient(90deg,#ffffff 0%,#eef2f4 25%,#dfe6ea 55%,#c9e0ee 75%,#6fb8e0 85%,#e4ebef 100%);
}
.header-rule{position:absolute;left:0;top:200px;width:100%;height:4px;background:var(--teal)}
.brand{position:absolute;left:18px;top:14px}
.brand-mark{position:absolute;left:197px;top:0;width:74px;height:74px;border-radius:50%;background:var(--teal-light)}
.brand-name{
  position:absolute;left:0;top:122px;white-space:nowrap;
  font-size:24px;font-weight:700;letter-spacing:2.6px;color:#2b2b2b;
}
.nav{position:absolute;left:18px;top:221px;width:214px;list-style:none;
  background:linear-gradient(180deg,var(--teal-light),var(--teal-dark));
  border-bottom-right-radius:12px;overflow:hidden}
.nav li{height:33px;line-height:32px;padding-left:11px;color:#fff;font-size:16.5px;border-bottom:1px solid rgba(255,255,255,.85)}
.nav li:last-child{border-bottom:none}
.nav li.active{font-weight:700}
.section-title{color:var(--teal);font-size:20px;font-weight:400;position:absolute}
.about-title{left:256px;top:225px}
.about-photo{position:absolute;left:257px;top:264px;width:157px;height:127px;
  background:radial-gradient(circle at 55% 50%,#f4f8fa 0%,#c7d8e0 55%,#8fb1c0 100%)}
.about-text{position:absolute;left:424px;top:262px;width:432px;font-size:15.5px;line-height:16.5px;text-align:justify;color:var(--text)}
.about-text p+p{margin-top:6px}
.about-claim{position:absolute;left:257px;top:399px;font-size:16px;font-weight:700;color:var(--text);letter-spacing:.3px}
.more{color:var(--teal);font-weight:700;font-size:14px}
.about-more{position:absolute;left:740px;top:428px}
.news-title{left:256px;top:465px}
.news{position:absolute;top:501px;width:277px}
.news-1{left:257px}.news-2{left:582px}
.news-photo{width:277px;height:119px;background:linear-gradient(90deg,#e9eef0 0%,#c6c2bd 30%,#eef1f2 55%,#bfc6cb 80%,#e8ecee 100%)}
.news h3{font-size:17px;font-weight:700;margin-top:14px;letter-spacing:.3px}
.news p{font-size:14px;line-height:18px;text-align:justify;margin-top:6px;color:var(--text)}
.news .more{display:block;text-align:right;margin-top:3px;padding-right:1px}
.events{position:absolute;left:882px;top:226px;width:207px}
.events h2{color:var(--teal);font-size:17.5px;font-weight:700;margin-bottom:12px}
.event{border-bottom:1px solid var(--rule);padding-bottom:4px;margin-bottom:12px;font-size:14.5px;line-height:17px}
.event:last-child{border-bottom:none}
.event strong{color:#444}
.event span{display:block;color:var(--muted)}
.event .more{font-size:14px}
.footer{position:absolute;left:0;top:823px;width:1200px;text-align:center;font-size:14px;color:var(--footer)}
</style>
</head>
<body>
<div class="page">
  <header class="header">
    <div class="header-photo" role="img" aria-label="Laborfoto: Reagenzgläser mit blauer Flüssigkeit"></div>
    <div class="brand">
      <div class="brand-mark"></div>
      <div class="brand-name">RHEINAU VITA FORSCHUNGSBUND</div>
    </div>
  </header>
  <div class="header-rule"></div>

  <ul class="nav">
    <li>» Startseite</li>
    <li class="active">» Über uns</li>
    <li>» Veranstaltungen</li>
    <li>» Aktuelles</li>
    <li>» Region</li>
    <li>» Service</li>
    <li>» Kontakt</li>
  </ul>

  <h2 class="section-title about-title">Über uns</h2>
  <div class="about-photo" role="img" aria-label="Foto: DNA-Doppelhelix unter einer Lupe"></div>
  <div class="about-text">
    <p>Der Rheinau Vita Forschungsbund versteht sich als Schritt&shy;macher für die Biotechnologie-Region Rhein-Main.</p>
    <p>Wir sind qualifizierter Ansprechpartner für Unternehmen, Politik und Medien und Interessen&shy;vertretung für alle, die in der Wertschöpfungskette von der Grundlagenforschung bis zum fertigen Produkt und seiner Vermarktung arbeiten.</p>
  </div>
  <p class="about-claim">Hierfür bieten wir ein in der Region einzigartiges Netzwerk.</p>
  <a class="more about-more">» mehr erfahren</a>

  <h2 class="section-title news-title">Aktuelles</h2>
  <article class="news news-1">
    <div class="news-photo" role="img" aria-label="Foto: Wissenschaftlerin am Mikroskop im Labor"></div>
    <h3>Meldung Eins</h3>
    <p>Lorem ipsum dolor sit amet, consetetur sadipscing elitr, sed diam nonumy eirmod tempor invidunt ut labore et dolore magna.</p>
    <a class="more">» mehr</a>
  </article>
  <article class="news news-2">
    <div class="news-photo" role="img" aria-label="Foto: Wissenschaftlerin am Mikroskop im Labor"></div>
    <h3>Meldung Zwei</h3>
    <p>Lorem ipsum dolor sit amet, consetetur sadipscing elitr, sed diam nonumy eirmod tempor invidunt ut labore et dolore magna.</p>
    <a class="more">» mehr</a>
  </article>

  <aside class="events">
    <h2>Veranstaltungen</h2>
    <div class="event"><strong>07.12.10 Veranstaltung Name</strong><span>Nummer 1 zum Thema X</span><a class="more">» mehr</a></div>
    <div class="event"><strong>10.12.10 Veranstaltung Name</strong><span>Nummer 2 zum Thema Y</span><a class="more">» mehr</a></div>
    <div class="event"><strong>24.12.10 Veranstaltung Name</strong><span>Nummer 3 zum Thema Z</span><a class="more">» mehr</a></div>
    <div class="event"><strong>07.01.11 Veranstaltung Name</strong><span>Nummer 1 zum Thema X</span><a class="more">» mehr</a></div>
    <div class="event"><strong>10.01.11 Veranstaltung Name</strong><span>Nummer 2 zum Thema Y</span><a class="more">» mehr</a></div>
    <div class="event"><strong>24.01.11 Veranstaltung Name</strong><span>Nummer 3 zum Thema Z</span><a class="more">» mehr</a></div>
  </aside>
</div>
<footer class="footer">© 2010 | Rheinau Vita Forschungsbund e.V. | Kontakt | Impressum</footer>
</body>
</html>
```